Lanternway 7.5 - Educational Guide/Course-pack/Worksheet

Our Lanternway 7.5 toolkit is an educational workshop that focuses on inspiring student initiatives in the classroom! We need a new educational course guide or course-pack for students/teachers that clearly outlines or explains the program steps, offers helpful tips and includes empty spaces/lines where their can write down their great ideas or notes. This will include a;

- Teachers Guide (1 Page)
- Student Guide/Worksheet (4 Pages)
- Group Pack Resources (3 Pages)

This will consist of designing/formatting text, stock animation/icons, font, etc. We have included our new logo (color, branding, etc.) and all of the text for each separate course-pack. We have also attached our new website to give you an idea of the program style.

Our workshop can be for any school project like Technology, Community, Environment, Art, Science, etc.

Target Market(s)

High School Students/Teachers

Industry/Entity Type

Education

Font styles to use
Sans Serif

Colors
f68e4e
acd037
34a7d8

Requirements
Must have
• Use our brand colors from logo.
Should not have
• Should not be too childish.

```html
<!DOCTYPE html>
<html lang="en">
<head>
<meta charset="utf-8">
<title>Lanternway 7.5 – Group Pack Resources</title>
<link href="https://fonts.googleapis.com/css2?family=Nunito:wght@300;400;600;700;800;900&display=swap" rel="stylesheet">
<style>
  :root{
    --backdrop:#4a4a4a;
    --paper:#ffffff;
    --brand-blue:#1a9dcb;
    --brand-orange:#f68e2a;
    --brand-green:#a9cf3a;
    --table-orange:#f26f21;
    --row-blue:#bfe3f0;
    --row-cream:#eef4d8;
    --row-blue-soft:#cde9f3;
    --ink:#1e1e1e;
    --ink-soft:#3a3a3a;
    --rule:#3b7fa1;
  }
  *{box-sizing:border-box;margin:0;padding:0}
  html,body{width:1200px;height:569px;overflow:hidden}
  body{background:linear-gradient(180deg,#555 0%,#3a3a3a 100%);font-family:"Nunito",sans-serif;color:var(--ink);position:relative}

  .page{position:absolute;top:28px;width:362px;height:512px;background:var(--paper);overflow:hidden}
  .page--group{left:31px}
  .page--money{left:419px}
  .page--letter{left:807px}

  .color-bar{position:absolute;top:0;height:6.5px;display:flex;left:0;width:362px}
  .color-bar span{display:block;height:100%}
  .color-bar .blue{background:var(--brand-blue);width:246px}
  .color-bar .orange{background:var(--brand-orange);width:61px}
  .color-bar .green{background:var(--brand-green);width:55px}

  /* group page */
  .group-topline{position:absolute;top:0;left:0;width:362px;height:12px;display:flex}
  .group-topline .white{width:246px;background:#fff}
  .group-topline .blue{width:60px;background:var(--brand-blue)}
  .group-topline .orange{width:56px;background:var(--brand-orange)}
  .hero{position:absolute;top:12px;left:0;width:362px;height:102px;background:var(--brand-green)}
  .hero-art{position:absolute;left:8px;top:8px;width:150px;height:94px;border-radius:40px 40px 0 0;
    background:radial-gradient(ellipse at 50% 40%,#f2b27a 0%,#e07a4b 40%,#3d5a7a 80%,rgba(61,90,122,0) 100%)}
  .hero-title{position:absolute;left:164px;top:17px;color:#fff;font-size:20.5px;font-weight:900;white-space:nowrap;line-height:1}
  .hero-title .light{font-weight:300}
  .hero-sub{position:absolute;left:166px;top:43px;color:#fff;font-size:15px;font-weight:300;line-height:1}
  .hero-tagline{position:absolute;left:166px;top:60px;color:#fff;font-size:15.5px;font-weight:900;line-height:16px;width:190px}

  .section-title{position:absolute;color:var(--brand-blue);font-weight:800;font-size:12px;white-space:nowrap}
  .who-title{left:51px;top:124px}
  .intro{position:absolute;left:51px;top:147px;font-size:5.2px;font-weight:600;line-height:7.4px;width:250px}
  .intro p+p{margin-top:6px}
  .intro .indent{padding-left:5px}

  table.grid{position:absolute;border-collapse:collapse;table-layout:fixed;font-size:5.4px;font-weight:700;text-align:center}
  table.grid th,table.grid td{border:0.5px solid var(--rule);padding:0;overflow:hidden;white-space:nowrap}
  table.grid tr:nth-child(odd) td{background:var(--row-cream)}
  table.grid tr:nth-child(even) td{background:var(--row-blue-soft)}

  .task-table{left:51px;top:188px;width:265px}
  .task-table th{background:var(--brand-blue);color:#fff;height:15px;font-weight:700}
  .task-table td{height:15.7px}

  /* money page */
  .money-title{left:0;width:362px;text-align:center;top:27px;font-size:12px}
  .label-caps{position:absolute;left:40px;top:60px;font-size:5.3px;font-weight:700}
  .money-intro{position:absolute;left:40px;top:74px;font-size:5.2px;font-weight:700;line-height:7.4px;width:300px}
  .fill-line{position:absolute;top:104px;font-size:5.3px;font-weight:700;display:flex;align-items:flex-end}
  .fill-line i{display:inline-block;border-bottom:0.5px solid #555;height:6px;margin-left:1px}

  .money-table{left:40px;width:282px}
  .money-table th{background:var(--table-orange);color:#fff;height:10.3px;font-weight:700}
  .money-table td{height:10.3px;font-weight:600}
  .money-table tr:nth-child(even) td{background:var(--row-blue)}
  .money-table.needs{top:130px}
  .money-table.supplies{top:271px}
  .money-table.balance{top:412px}

  /* letter page */
  .letter{position:absolute;left:51px;width:265px;font-size:6.1px;line-height:9.1px;color:var(--ink-soft)}
  .letter strong{color:var(--ink);font-weight:700}
  .letter-field{display:flex;align-items:flex-end;width:265px}
  .letter-field i{flex:1;border-bottom:0.5px solid #888;height:5px;margin-left:6px}
  .contact-list{list-style:none}
  .contact-list li{position:relative;padding-left:5px}
  .contact-list li::before{content:"";position:absolute;left:0;top:3.4px;width:2px;height:2px;background:var(--brand-green)}

  .wordmark{position:absolute;left:46px;top:455px;display:flex;align-items:center;gap:7px}
  .wordmark .dot{width:28px;height:28px;border-radius:50%;background:var(--brand-blue)}
  .wordmark .name{font-size:16px;font-weight:700;color:#555;line-height:1}
</style>
</head>
<body>

<!-- Group page -->
<section class="page page--group">
  <div class="group-topline"><span class="white"></span><span class="blue"></span><span class="orange"></span></div>
  <header class="hero">
    <div class="hero-art" role="img" aria-label="Illustration of a diverse group of smiling students waving"></div>
    <h1 class="hero-title">The G-Pack <span class="light">(Group)</span></h1>
    <p class="hero-sub">The Lanternway 7.5</p>
    <p class="hero-tagline">Your Project-Launching Workshop</p>
  </header>

  <h2 class="section-title who-title">Who Does What?</h2>
  <div class="intro">
    <p>You can use the ‘Who Does What?’ in two ways.</p>
    <p>1. Make and update a list of all the things the whole group needs to do.<br>
    2. Each person in the group can use it to keep track of everything that needs to be done in<br>
    <span class="indent">their “committee”.&nbsp; Ex. Marketing, fund-raising, or production.</span></p>
  </div>

  <table class="grid task-table">
    <colgroup><col style="width:82px"><col style="width:90px"><col style="width:93px"></colgroup>
    <thead><tr><th>Task</th><th>Who will do it?</th><th>When will you do it?</th></tr></thead>
    <tbody>
      <tr><td></td><td></td><td></td></tr><tr><td></td><td></td><td></td></tr>
      <tr><td></td><td></td><td></td></tr><tr><td></td><td></td><td></td></tr>
      <tr><td></td><td></td><td></td></tr><tr><td></td><td></td><td></td></tr>
      <tr><td></td><td></td><td></td></tr><tr><td></td><td></td><td></td></tr>
      <tr><td></td><td></td><td></td></tr><tr><td></td><td></td><td></td></tr>
      <tr><td></td><td></td><td></td></tr><tr><td></td><td></td><td></td></tr>
      <tr><td></td><td></td><td></td></tr><tr><td></td><td></td><td></td></tr>
      <tr><td></td><td></td><td></td></tr><tr><td></td><td></td><td></td></tr>
      <tr><td></td><td></td><td></td></tr><tr><td></td><td></td><td></td></tr>
    </tbody>
  </table>
</section>

<!-- Money page -->
<section class="page page--money">
  <div class="color-bar"><span class="blue"></span><span class="orange"></span><span class="green"></span></div>
  <h2 class="section-title money-title">The Money Machines</h2>
  <p class="label-caps">FINANCIAL NEEDS</p>
  <p class="money-intro">Make money your friend- not your enemy!&nbsp; You’ve got to know what you need and how much it costs!<br>Ex.&nbsp; Doers realize that they will need 6 soccer-balls, 100 drinks, 2 referee sweaters, etc.</p>
  <p class="fill-line" style="left:40px">Project Name:<i style="width:134px"></i></p>
  <p class="fill-line" style="left:214px">Date:<i style="width:87px"></i></p>

  <table class="grid money-table needs">
    <colgroup><col style="width:122px"><col style="width:89px"><col style="width:71px"></colgroup>
    <thead><tr><th>Item</th><th>Amount</th><th>Total</th></tr></thead>
    <tbody>
      <tr><td>Sponsorships or Donations</td><td></td><td>$&nbsp; 500</td></tr>
      <tr><td>School Help</td><td></td><td>$&nbsp; 50</td></tr>
      <tr><td>Sales</td><td></td><td>$&nbsp; 100</td></tr>
      <tr><td></td><td></td><td></td></tr><tr><td></td><td></td><td></td></tr>
      <tr><td></td><td></td><td></td></tr><tr><td></td><td></td><td></td></tr>
      <tr><td></td><td></td><td></td></tr><tr><td></td><td></td><td></td></tr>
      <tr><td></td><td></td><td></td></tr>
      <tr><td></td><td>Total $ Needed</td><td></td></tr>
    </tbody>
  </table>

  <table class="grid money-table supplies">
    <colgroup><col style="width:86px"><col style="width:36px"><col style="width:90px"><col style="width:70px"></colgroup>
    <thead><tr><th>Item</th><th>Quantity</th><th>Cost</th><th>Total</th></tr></thead>
    <tbody>
      <tr><td>Soccer balls</td><td>6</td><td>Free from school</td><td>$&nbsp; 0</td></tr>
      <tr><td>Drinks</td><td>100</td><td>50 cents</td><td>$&nbsp; 00</td></tr>
      <tr><td></td><td></td><td></td><td></td></tr><tr><td></td><td></td><td></td><td></td></tr>
      <tr><td></td><td></td><td></td><td></td></tr><tr><td></td><td></td><td></td><td></td></tr>
      <tr><td></td><td></td><td></td><td></td></tr><tr><td></td><td></td><td></td><td></td></tr>
      <tr><td></td><td></td><td></td><td></td></tr>
      <tr><td></td><td></td><td>Total $ Needed</td><td></td></tr>
    </tbody>
  </table>

  <table class="grid money-table balance">
    <colgroup><col style="width:122px"><col style="width:89px"><col style="width:71px"></colgroup>
    <thead><tr><th>Item</th><th>Amount</th><th>Total</th></tr></thead>
    <tbody>
      <tr><td>Income</td><td></td><td></td></tr>
      <tr><td>Expenses</td><td></td><td></td></tr>
      <tr><td></td><td></td><td></td></tr>
      <tr><td>(Total 1 – Total 2)</td><td>Total $ Needed</td><td></td></tr>
    </tbody>
  </table>
</section>

<!-- Letter page -->
<section class="page page--letter">
  <div class="color-bar"><span class="blue"></span><span class="orange"></span><span class="green"></span></div>

  <p class="letter" style="top:76px">DATE</p>
  <p class="letter" style="top:104px">Dear Mr./Ms. Name,</p>
  <p class="letter" style="top:122px">We sincerely appreciate Company or Organization’s Name dedication to supporting youth initiatives in the community and are thankful for the opportunity to submit our donation request!<br>
  We at School/Org Name are hoping to help, promote and support our cause by Organizing / Launching/Etc. a Project Name in our local community. With this in mind, we are currently seeking donations and/or sponsorships which would aid our effort. Our project will focus on Describe Project Target &amp; Objectives.</p>
  <p class="letter" style="top:195px">We sincerely feel that you would be a great fit with our initiative and are respectfully requesting Donation Amount/Materials.</p>
  <p class="letter" style="top:222px"><strong>Project/Event Details</strong></p>
  <p class="letter letter-field" style="top:240px"><strong>Project Name:</strong><i></i></p>
  <p class="letter letter-field" style="top:258px"><strong>Location of Event:</strong><i></i></p>
  <p class="letter" style="top:276px">Your support would be an invaluable partnership and your donation will directly impact our goal! Thank you and please feel free to reach out if you have any additional questions about the project or our organization.</p>
  <p class="letter" style="top:313px">Kind regards,</p>
  <p class="letter" style="top:331px"><strong>Your Name</strong></p>
  <ul class="letter contact-list" style="top:349px">
    <li>School or Organization Name</li>
    <li>Your Phone Number</li>
    <li>Your Email</li>
  </ul>

  <div class="wordmark">
    <span class="dot"></span>
    <span class="name">Lanternway 7.5</span>
  </div>
</section>

</body>
</html>
```